Business Card Design Project and Logo Enhancement

This project requires designing a business card for a construction company. It also requires small enhancements on provided logo.
Summary about the company:
Name: Velmoria Group.
Future website. www.velmoria.ca
Velmoria is a home redesign and renovation company providing services in Ottawa Canada area.
It offers the following services:
- Home Additions
- Roofing
- Eavestroughing & Soffit Fascia
- Fencing
- Decks
- Window Installation, and
- Indoor Renovation Including ( Kitchen redesign, Basement finishing, bathroom upgrades, etc)
Logo and Company name background:
Velmoria refers to an ancient empire that was located in Balkans called Velmorians.
Provided logo represents the symbol of Velmorians.
Project Expectation:
Logo:
Attached logo is too SIMPLe. It would be nice adding a bit of design.
That could include different colors or adding a bit of style to the logo.
Business Card
Initial preferred layout/content ( open to other suggestions) :
Preferred type: Vertical with rounded corners
Front side should have:
- Logo
- Company Name
- First Name/ Last name: Ie: Luan Metreci
- Office Phone:
- Direct Phone:
- QR Code linking to www.velmoria.ca, and
- website url. www. velmoria.ca
Back end shall contain:
Professional services offered:
- Large company logo covering most of the card as a water mark
- Divisions Services offered
- Roofing
- Eavestroughing, Soffit, Fascia
- Fencing and Decks
- Indoor Design and Renovation
- Company Phone and
- Company website address: www.velmoria.ca
PSD and other raw files must be provided by the winner.

```html
<!DOCTYPE html>
<html lang="en">
<head>
<meta charset="utf-8">
<title>Velmoria Group – Business Card</title>
<link rel="stylesheet" href="https://fonts.googleapis.com/css2?family=Cinzel:wght@500&family=Jost:wght@500&family=Open+Sans:wght@400&display=swap">
<style>
  :root {
    --page-bg: #ffffff;
    --card-bg: #000000;
    --gold: #c9a24a;
    --gold-light: #f4e39a;
    --gold-deep: #b8861c;
    --text-light: #ffffff;
  }
  html, body {
    margin: 0;
    padding: 0;
    width: 1200px;
    height: 900px;
    overflow: hidden;
    background: var(--page-bg);
  }
  .canvas {
    position: relative;
    width: 1200px;
    height: 900px;
  }
  .card {
    position: absolute;
    left: 347px;
    top: 58px;
    width: 506px;
    height: 783px;
    border-radius: 38px;
    background: var(--card-bg);
    color: var(--text-light);
  }
  .brand-disc {
    position: absolute;
    left: 150px;
    top: 51px;
    width: 192px;
    height: 192px;
    border-radius: 50%;
    background: linear-gradient(90deg, var(--gold-deep) 0%, var(--gold-light) 50%, var(--gold-deep) 100%);
  }
  .brand-name {
    position: absolute;
    left: 0;
    top: 270px;
    width: 526px;
    margin: 0;
    text-align: center;
    font-family: "Cinzel", serif;
    font-weight: 500;
    font-size: 45px;
    letter-spacing: 1px;
    color: var(--gold);
    line-height: 1;
  }
  .person-name {
    position: absolute;
    left: 0;
    top: 426px;
    width: 490px;
    margin: 0;
    text-align: center;
    font-family: "Jost", sans-serif;
    font-weight: 500;
    font-size: 30px;
    line-height: 1;
    letter-spacing: 0.3px;
  }
  .contact-list {
    position: absolute;
    left: 59px;
    top: 564px;
    margin: 0;
    padding: 0;
    list-style: none;
    font-family: "Open Sans", sans-serif;
    font-size: 22px;
    line-height: 48px;
    letter-spacing: 0.4px;
  }
  .contact-label {
    display: inline-block;
  }
  .contact-label.fixed {
    width: 148px;
  }
  .contact-value {
    margin-left: 8px;
  }
</style>
</head>
<body>
  <div class="canvas">
    <div class="card">
      <div class="brand-disc"></div>
      <h1 class="brand-name">Velmoria Group</h1>
      <p class="person-name">Luan METRECI</p>
      <ul class="contact-list">
        <li><span class="contact-label">office phone:</span><span class="contact-value">000 000 000 00</span></li>
        <li><span class="contact-label">direct phone:</span><span class="contact-value">000 000 000 00</span></li>
        <li><span class="contact-label fixed">QR code</span>:<span class="contact-value">0000000</span></li>
        <li><span class="contact-label fixed">web</span>:<span class="contact-value">www. velmoria.ca</span></li>
      </ul>
    </div>
  </div>
</body>
</html>
```